New Website for Crime Scene Cleaner required

I need someone to create a complete new website and can set up SEO for me through the Website Designer or a third party for me. I have Logo that i will upload shortly once finalized for the website. I have domain names already but will need to be registered by the winner(i can supply the details I have received from HostMarlo). I am looking for a website that stands out but is simple and elegant, easy to navigate and use yet not boring. Using information provided by me for wording to create it as a stand out website. in total i am looking at 5-7 pages (About/Home, Fire & Smoke Restoration, Water Restoration/Mould Remediation, Crime Scene Cleaners, Methamphetamine Remediation/ Testing Services, Hoarding & Squalor Cleaning, Contact Us/Testimonials)This will be a start to finish project. I would like assistance to have it set up user friendly on mobile devices etc or refer a third party who can assist. Must be able to provide ongoing support when required by myself if the successful winner (i understand this will be an additional fee if required in the future).
You will also require to assist me with the email set up for the website so that it is fully functional or provide a third party who can.
To gain some information about the business you can visit my old website at www.pelbrookcove.com.au and welcome to use some of the wording from there for your entry.
It's been 14yrs since i've had a website made from me so suggestions are welcome if not mentioned in the scope as I want the website to be great.

I have uploaded 2 Logo's and a 3D Logo will come through shortly.

Target Market(s)

People affected by a traumatic event in their lives needing assistance by professionals who are understanding and professionally trained

Coding

Coded - Design and coding required

Requirements
Must have
• *** Please note that correct wording for pages will only be supplied upon a successful winner for the finalization of the project.

I have domain names already but will need to be registered by the winner(i can supply the details I have received from HostMarlo).
Nice to have
• the feeling that we care because we do and that we are passionate for what we do.

```html
<!DOCTYPE html>
<html lang="en">
<head>
<meta charset="utf-8">
<title>Halvard Trauma &amp; Decon Services</title>
<link href="https://fonts.googleapis.com/css2?family=Lato:wght@400;700;900&display=swap" rel="stylesheet">
<style>
:root{
  --orange:#f26a21;
  --orange-dark:#d9531a;
  --ink:#222;
  --muted:#666;
  --grey-bg:#f1f1f1;
  --dark:#1c1c1c;
  --white:#fff;
  --gold:#e8a21d;
}
*{box-sizing:border-box;margin:0;padding:0}
html,body{width:1200px;height:5368px;overflow:hidden}
body{font-family:"Lato",Arial,sans-serif;color:var(--ink);background:var(--white);position:relative}
section,header,footer{position:absolute;left:0;width:1200px}
.btn{display:inline-block;background:var(--orange);color:var(--white);font-size:12px;font-weight:700;padding:9px 22px;border-radius:20px;letter-spacing:.5px}
.section-title{position:absolute;left:0;width:1200px;text-align:center;font-size:30px;font-weight:700;letter-spacing:1px}
.title-mark{position:absolute;left:590px;width:20px;height:20px}
.body-text{font-size:13px;line-height:1.7;color:var(--muted)}

/* hero */
.hero{top:0;height:780px;background:linear-gradient(120deg,#3a2a3e 0%,#5b4c70 40%,#2a2430 100%)}
.hero-photo{position:absolute;inset:0;background:radial-gradient(ellipse at 70% 40%,#8f87b5 0%,#4a3f5e 45%,#1e1a24 100%);opacity:.9}
.brand{position:absolute;left:120px;top:30px;display:flex;align-items:center;gap:10px;color:var(--white);font-size:18px;font-weight:900;letter-spacing:.5px}
.brand-dot{width:28px;height:28px;border-radius:50%;background:var(--orange)}
.topbar{position:absolute;left:860px;top:0;width:340px;height:50px;background:var(--orange);display:flex;align-items:center;gap:24px;padding-left:30px;color:var(--white);font-size:11px}
.topbar span{display:flex;align-items:center;gap:6px}
.main-nav{position:absolute;left:530px;top:62px;width:670px;height:48px;background:rgba(242,106,33,.85);display:flex;align-items:center;gap:36px;padding-left:30px;color:var(--white);font-size:13px;font-weight:700}
.hero-title{position:absolute;left:120px;top:270px;color:var(--white);font-size:38px;font-weight:700;line-height:1.15;letter-spacing:1px}
.hero-sub{position:absolute;left:120px;top:370px;color:var(--white);font-size:13px}
.hero .btn{position:absolute;left:120px;top:402px}
.hero-wave{position:absolute;left:0;top:650px}

/* about */
.about{top:780px;height:600px}
.about-photo{position:absolute;left:150px;top:100px;width:460px;height:460px;border-radius:50%;background:radial-gradient(circle at 50% 45%,#b58a5e 0%,#6e4d33 60%,#3a2a1e 100%)}
.badge{position:absolute;left:440px;top:330px;width:150px;height:150px;border-radius:50%;background:var(--gold);border:6px solid var(--white)}
.about h2{position:absolute;left:640px;top:90px;font-size:30px;letter-spacing:1px}
.about .body-text{position:absolute;left:640px;top:150px;width:470px}
.about .btn{position:absolute;left:640px;top:470px}

/* services */
.services{top:1392px;height:790px;background:var(--grey-bg)}
.card{position:absolute;top:180px;width:294px;height:430px;background:var(--white);border-radius:6px;box-shadow:0 4px 14px rgba(0,0,0,.1);text-align:center}
.card-photo{height:190px;border-radius:6px 6px 0 0}
.card-icon{width:22px;height:22px;margin:16px auto 8px}
.card h3{font-size:14px;font-weight:700}
.card .body-text{padding:10px 40px;font-size:12px}
.card .more{color:var(--orange);font-size:11px;font-weight:700;text-decoration:underline}
.arrow{position:absolute;top:370px;width:34px;height:34px;border-radius:50%;background:var(--white);box-shadow:0 2px 6px rgba(0,0,0,.15);display:flex;align-items:center;justify-content:center}
.services .btn{position:absolute;left:530px;top:688px}

/* video */
.video{top:2192px;height:510px;background:radial-gradient(ellipse at 30% 40%,#c9c9d2 0%,#6e6f7a 40%,#2b2d35 100%)}
.play{position:absolute;left:560px;top:215px;width:80px;height:80px;border-radius:50%;background:rgba(255,255,255,.9);display:flex;align-items:center;justify-content:center}

/* why */
.why{top:2712px;height:780px}
.feature{position:absolute;width:300px;text-align:center}
.feature-icon{width:56px;height:56px;margin:0 auto 12px;border-radius:50%;background:var(--orange);display:flex;align-items:center;justify-content:center}
.feature h3{font-size:14px;font-weight:700;line-height:1.3}
.feature .body-text{font-size:12px;margin-top:8px}

/* banner */
.banner{top:3492px;height:470px;background:var(--dark);overflow:hidden}
.banner-photo{position:absolute;left:560px;top:0;width:640px;height:470px;background:linear-gradient(100deg,#5f6470 0%,#c9ccd2 55%,#eef0f2 100%)}
.banner h2{position:absolute;left:120px;top:70px;color:var(--white);font-size:28px;line-height:1.2;letter-spacing:.5px;white-space:nowrap}
.banner .body-text{position:absolute;left:120px;top:160px;width:440px;color:#ddd}
.banner .btn{position:absolute;left:120px;top:290px}
.banner-curve{position:absolute;left:0;top:0}

/* reviews */
.reviews{top:3990px;height:420px}
.quote{position:absolute;top:150px;font-size:60px;color:#555;font-weight:900}
.review-text{position:absolute;left:200px;top:160px;width:800px;text-align:center}
.stars{position:absolute;left:0;width:1200px;top:262px;text-align:center;color:var(--gold);font-size:14px;letter-spacing:2px}
.reviewer{position:absolute;left:0;width:1200px;top:285px;text-align:center;font-size:18px;font-weight:700;letter-spacing:1px}
.dots{position:absolute;left:570px;top:325px;display:flex;gap:8px}
.dots i{width:10px;height:10px;border-radius:50%;background:#333}
.dots i:first-child{background:var(--orange)}

/* contact */
.contact{top:4410px;height:560px}
.field{position:absolute;height:40px;background:#f4f4f4;border-radius:20px;font-size:11px;color:#999;padding:12px 20px}
.contact .btn{position:absolute;left:560px;top:470px}

/* footer */
.site-footer{top:4960px;height:408px;background:var(--dark);color:var(--white)}
.footer-wave{position:absolute;left:0;top:0}
.foot-col{position:absolute;top:130px;font-size:12px;line-height:1.8}
.foot-col h4{font-size:14px;letter-spacing:1px;margin-bottom:12px}
.newsletter-input{width:240px;height:32px;border-radius:16px;background:var(--white);color:#999;font-size:11px;padding:8px 16px}
.newsletter .btn{margin-top:10px}
.socials{display:flex;gap:8px;margin-top:16px}
.socials i{width:22px;height:22px;border-radius:50%;background:var(--orange)}
.copyright{position:absolute;left:0;bottom:0;width:1200px;height:48px;border-top:1px solid #333;display:flex;align-items:center;padding-left:120px;font-size:11px;color:#bbb}
</style>
</head>
<body>

<header class="hero">
  <div class="hero-photo" role="img" aria-label="Technician in a protective suit cleaning a room with equipment cases"></div>
  <div class="brand"><span class="brand-dot"></span>Halvard Trauma &amp; Decon</div>
  <div class="topbar">
    <span><svg width="12" height="12" viewBox="0 0 24 24"><path fill="#fff" d="M6.6 10.8a15 15 0 006.6 6.6l2.2-2.2a1 1 0 011-.2 11 11 0 003.6.6 1 1 0 011 1V20a1 1 0 01-1 1A17 17 0 013 4a1 1 0 011-1h3.5a1 1 0 011 1 11 11 0 00.6 3.6 1 1 0 01-.3 1z"/></svg>+00 555 019 284</span>
    <span><svg width="12" height="12" viewBox="0 0 24 24"><path fill="#fff" d="M2 5h20v14H2zm2 2v.5l8 5 8-5V7z"/></svg>info@halvardtrauma.com</span>
  </div>
  <nav class="main-nav"><span>HOME</span><span>ABOUT US</span><span>SERVICES</span><span>TESTIMONIALS</span><span>CONTACT US</span></nav>
  <h1 class="hero-title">TRUSTED<br>TRAUMA &amp; DECON SERVICES</h1>
  <p class="hero-sub">24/7 Crime Scene Cleaning service</p>
  <a class="btn">READ MORE</a>
  <svg class="hero-wave" width="1200" height="130" viewBox="0 0 1200 130">
    <path d="M0 70 Q600 150 1200 40 L1200 130 L0 130Z" fill="var(--orange)"/>
    <path d="M0 95 Q600 160 1200 70 L1200 130 L0 130Z" fill="#fff"/>
  </svg>
</header>

<section class="about">
  <div class="about-photo" role="img" aria-label="Gloved hands cleaning a stained surface"></div>
  <div class="badge" role="img" aria-label="Years of experience seal"></div>
  <h2>ABOUT US</h2>
  <div class="body-text">
    <p>Our trained team arrives quickly and treats every home with respect. We clean, sanitise and restore spaces after trauma, fire, flood and neglect, so families can focus on healing while we handle the hard work with care, discretion and professional skill every time.</p>
    <p style="margin-top:14px">We have served our community for fourteen years, using approved methods and safe products. Every job is planned around your needs, with clear pricing, honest advice and ongoing support until the space is safe, clean and ready to live in again.</p>
  </div>
  <a class="btn">READ MORE</a>
</section>

<section class="services">
  <h2 class="section-title" style="top:70px">OUR SERVICES</h2>
  <svg class="title-mark" style="top:115px" viewBox="0 0 20 20"><path d="M10 1c2 4 6 6 6 11a6 6 0 01-12 0c0-3 2-4 3-7 1 2 2 3 3 3 0-3 0-5 0-7z" fill="var(--orange)"/></svg>
  <div class="arrow" style="left:80px"><svg width="10" height="10" viewBox="0 0 10 10"><path d="M7 1L3 5l4 4" stroke="#333" fill="none" stroke-width="1.5"/></svg></div>
  <div class="arrow" style="left:1116px"><svg width="10" height="10" viewBox="0 0 10 10"><path d="M3 1l4 4-4 4" stroke="#333" fill="none" stroke-width="1.5"/></svg></div>

  <div class="card" style="left:120px">
    <div class="card-photo" role="img" aria-label="Fire damaged building facade" style="background:linear-gradient(180deg,#b9b6c4,#5a4f4a)"></div>
    <svg class="card-icon" viewBox="0 0 20 20"><path d="M10 1c2 4 6 6 6 11a6 6 0 01-12 0c0-3 2-4 3-7 1 2 2 3 3 3 0-3 0-5 0-7z" fill="var(--orange)"/></svg>
    <h3>FIRE &amp; SMOKE RESTORATION</h3>
    <p class="body-text">Smoke and soot are removed with care, and rooms are restored to a safe state.</p>
    <span class="more">READ MORE</span>
  </div>
  <div class="card" style="left:452px">
    <div class="card-photo" role="img" aria-label="Mould growing on a water damaged wall" style="background:linear-gradient(180deg,#e5e5e2,#8a8f84)"></div>
    <svg class="card-icon" viewBox="0 0 20 20"><path d="M10 1c3 5 6 8 6 12a6 6 0 01-12 0c0-4 3-7 6-12z" fill="var(--orange)"/></svg>
    <h3>WATER RESTORATION/MOULD<br>REMEDIATION</h3>
    <p class="body-text">Water is extracted and mould is treated so the home is dry and healthy.</p>
    <span class="more">READ MORE</span>
  </div>
  <div class="card" style="left:784px">
    <div class="card-photo" role="img" aria-label="Cluttered room filled with hoarded belongings" style="background:linear-gradient(180deg,#b48a4e,#5d4530)"></div>
    <svg class="card-icon" viewBox="0 0 20 20"><path d="M2 9l8-7 8 7v9H2z" fill="var(--orange)"/></svg>
    <h3>HOARDING &amp; SQUALOR CLEANING</h3>
    <p class="body-text">Cluttered homes are cleared and cleaned at a pace that respects the owner.</p>
    <span class="more">READ MORE</span>
  </div>
  <a class="btn">VIEW ALL SERVICES</a>
</section>

<section class="video" role="img" aria-label="Video still of a gloved technician cleaning a glass door">
  <div class="play"><svg width="28" height="28" viewBox="0 0 28 28"><path d="M9 6l14 8-14 8z" fill="var(--orange)"/></svg></div>
</section>

<section class="why">
  <h2 class="section-title" style="top:60px">WHY CHOOSE US</h2>
  <svg class="title-mark" style="top:105px" viewBox="0 0 20 20"><path d="M10 1c2 4 6 6 6 11a6 6 0 01-12 0c0-3 2-4 3-7 1 2 2 3 3 3 0-3 0-5 0-7z" fill="var(--orange)"/></svg>

  <div class="feature" style="left:150px;top:200px"><div class="feature-icon"><svg width="26" height="26" viewBox="0 0 24 24"><circle cx="12" cy="8" r="4" fill="#fff"/><path d="M4 21c0-5 4-7 8-7s8 2 8 7z" fill="#fff"/></svg></div><h3>TRUSTED, EXPERIENCED<br>PROFESSIONALS</h3><p class="body-text">Our trained staff bring years of field experience to every job we take on.</p></div>
  <div class="feature" style="left:450px;top:200px"><div class="feature-icon"><svg width="26" height="26" viewBox="0 0 24 24"><circle cx="12" cy="12" r="9" fill="none" stroke="#fff" stroke-width="2"/><path d="M12 7v5l3 3" stroke="#fff" stroke-width="2" fill="none"/></svg></div><h3>24/7 EMERGENCY<br>CLEANUP SERVICES</h3><p class="body-text">Call any hour of the day or night and our team will respond quickly.</p></div>
  <div class="feature" style="left:750px;top:200px"><div class="feature-icon"><svg width="26" height="26" viewBox="0 0 24 24"><path d="M5 12l5 5 9-10" stroke="#fff" stroke-width="2.5" fill="none"/></svg></div><h3>100% CUSTOMER<br>SATISFACTION GUARANTEED</h3><p class="body-text">We stay until the job is done right and you are fully happy with it.</p></div>
  <div class="feature" style="left:150px;top:480px"><div class="feature-icon"><svg width="26" height="26" viewBox="0 0 24 24"><path d="M3 11l9-8 9 8v10H3z" fill="#fff"/></svg></div><h3>FAMILY OWNED AND<br>OPERATED COMPANY</h3><p class="body-text">A local family business that treats every client like a neighbour.</p></div>
  <div class="feature" style="left:450px;top:480px"><div class="feature-icon"><svg width="26" height="26" viewBox="0 0 24 24"><circle cx="12" cy="12" r="9" fill="#fff"/><path d="M12 7v10M9 9h5a2 2 0 010 4h-4a2 2 0 000 4h5" stroke="var(--orange)" stroke-width="1.5" fill="none"/></svg></div><h3>COST-EFFECTIVE<br>CRIME SCENE CLEANING</h3><p class="body-text">Clear and fair pricing with no hidden fees or surprise charges.</p></div>
  <div class="feature" style="left:750px;top:480px"><div class="feature-icon"><svg width="26" height="26" viewBox="0 0 24 24"><path d="M12 2l8 3v6c0 5-3.5 9-8 11-4.5-2-8-6-8-11V5z" fill="#fff"/></svg></div><h3>LICENSED, INSURED<br>AND HIGHLY TRAINED</h3><p class="body-text">Fully licensed and insured crews trained to strict safety standards.</p></div>
</section>

<section class="banner">
  <div class="banner-photo" role="img" aria-label="Technician in protective suit and respirator"></div>
  <svg class="banner-curve" width="1200" height="470" viewBox="0 0 1200 470">
    <path d="M0 0 H650 Q520 240 700 470 H0Z" fill="var(--dark)"/>
    <path d="M650 0 Q520 240 700 470" stroke="var(--orange)" stroke-width="10" fill="none"/>
    <path d="M0 420 Q300 380 560 470 H0Z" fill="var(--orange)"/>
  </svg>
  <h2>CRIME SCENE CLEANING COMPANY<br>THAT CARES</h2>
  <p class="body-text">We know these are some of the hardest moments in life. Our team works quietly and carefully, restoring your space so you can focus on family and recovery while we handle every detail with compassion and skill.</p>
  <a class="btn">CONTACT US NOW</a>
</section>

<section class="reviews">
  <h2 class="section-title" style="top:70px">CLIENT`S REVIEWS</h2>
  <svg class="title-mark" style="top:115px" viewBox="0 0 20 20"><path d="M10 1c2 4 6 6 6 11a6 6 0 01-12 0c0-3 2-4 3-7 1 2 2 3 3 3 0-3 0-5 0-7z" fill="var(--orange)"/></svg>
  <span class="quote" style="left:165px">&ldquo;</span>
  <span class="quote" style="left:1005px;top:200px">&rdquo;</span>
  <p class="review-text body-text">The team arrived within hours and handled everything with such kindness. They explained each step, worked quietly and left the home spotless. I could not have asked for more caring people during such a hard time for our family. Thank you all.</p>
  <div class="stars">★★★★★</div>
  <div class="reviewer">MARCUS DELANEY</div>
  <div class="dots"><i></i><i></i><i></i><i></i></div>
</section>

<section class="contact">
  <h2 class="section-title" style="top:110px">CONTACT US</h2>
  <svg class="title-mark" style="top:155px" viewBox="0 0 20 20"><path d="M10 1c2 4 6 6 6 11a6 6 0 01-12 0c0-3 2-4 3-7 1 2 2 3 3 3 0-3 0-5 0-7z" fill="var(--orange)"/></svg>
  <div class="field" style="left:320px;top:210px;width:272px">Full Name*</div>
  <div class="field" style="left:608px;top:210px;width:272px">Phone*</div>
  <div class="field" style="left:320px;top:268px;width:560px">Email Address*</div>
  <div class="field" style="left:320px;top:326px;width:560px;height:110px">Your Message*</div>
  <a class="btn">SEND NOW</a>
</section>

<footer class="site-footer">
  <svg class="footer-wave" width="1200" height="80" viewBox="0 0 1200 80">
    <path d="M0 0 H1200 V10 Q600 90 0 20Z" fill="#fff"/>
    <path d="M0 20 Q600 90 1200 10 V30 Q600 100 0 40Z" fill="var(--orange)"/>
  </svg>
  <div class="foot-col" style="left:120px;width:220px">
    <div style="display:flex;align-items:center;gap:8px;font-size:15px;font-weight:900;margin-bottom:14px"><span class="brand-dot" style="width:22px;height:22px"></span>Halvard</div>
    <p>Caring trauma and decon cleaning for homes and businesses in our region.</p>
  </div>
  <div class="foot-col" style="left:410px">
    <h4>QUICK LINKS</h4>
    <p>Home<br>About us<br>Services<br>Testimonials<br>Contact us</p>
  </div>
  <div class="foot-col" style="left:590px;width:220px">
    <h4>CONTACT INFO</h4>
    <p>+00 555 019 284<br>info@halvardtrauma.com<br>14 Ridge Lane,<br>Harbourside, 2041</p>
  </div>
  <div class="foot-col newsletter" style="left:850px">
    <h4>NEWSLETTER</h4>
    <div class="newsletter-input">Email Address</div>
    <a class="btn">SUBSCRIBE</a>
    <div class="socials"><i></i><i></i><i></i><i></i><i></i></div>
  </div>
  <div class="copyright">Copyright © 2020 Halvard Trauma &amp; Decon Services All Rights Reserved.</div>
</footer>

</body>
</html>
```